Silver Brook Home Business Cards

We need Business cards development for our expanding business. Our Company SilverBrookHome promotes grain free living through products, services and healthy living concepts. Our Products are:
Non-Grain
Non- GMO
Non- Soy
Gluten-Free

Project Deadline Extended
Reason: We will need to extend the deadline on our Business Card contest. Thanks, SBH

```html
<!DOCTYPE html>
<html lang="en">
<head>
<meta charset="utf-8">
<title>Silver Brook Home – Business Card</title>
<link rel="stylesheet" href="https://fonts.googleapis.com/css2?family=PT+Sans:wght@400;700&family=PT+Sans+Narrow:wght@400;700&display=swap">
<style>
  :root {
    --card-green: #3aaf4a;
    --deep-green: #0f5a2a;
    --brand-green: #1d7a36;
    --shadow-green: #1f6b2e;
    --paper: #ffffff;
    --ink-light: #ffffff;
  }
  html, body {
    margin: 0;
    padding: 0;
    width: 1200px;
    height: 703px;
    overflow: hidden;
    background: var(--paper);
  }
  .card {
    position: relative;
    width: 1200px;
    height: 703px;
    background: var(--card-green);
    font-family: "PT Sans Narrow", "Arial Narrow", sans-serif;
    color: var(--ink-light);
    overflow: hidden;
  }
  .mission {
    position: absolute;
    left: 137px;
    top: 44px;
    margin: 0;
    font-size: 41px;
    font-weight: 400;
    line-height: 1.1;
    color: var(--deep-green);
    white-space: nowrap;
  }
  .brand-shadow {
    position: absolute;
    left: 60px;
    top: 266px;
  }
  .brand-band {
    position: absolute;
    left: 49px;
    top: 133px;
    width: 1129px;
    height: 134px;
    background: var(--paper);
  }
  .brand-name {
    position: absolute;
    left: 0;
    top: 158px;
    width: 1227px;
    margin: 0;
    text-align: center;
    font-family: "PT Sans", Arial, sans-serif;
    font-weight: 700;
    font-size: 98px;
    line-height: 1;
    color: var(--brand-green);
    white-space: nowrap;
  }
  .person-name {
    position: absolute;
    left: 137px;
    top: 403px;
    margin: 0;
    font-family: "PT Sans Narrow", sans-serif;
    font-weight: 700;
    font-size: 66px;
    line-height: 1;
    color: var(--deep-green);
  }
  .person-title {
    position: absolute;
    left: 338px;
    top: 468px;
    margin: 0;
    font-size: 28px;
    line-height: 1;
    color: var(--deep-green);
  }
  .contact-list {
    position: absolute;
    left: 134px;
    top: 524px;
    margin: 0;
    padding: 0;
    list-style: none;
  }
  .contact-item {
    display: flex;
    align-items: center;
    height: 45px;
    font-family: "PT Sans", Arial, sans-serif;
    font-size: 34px;
    white-space: nowrap;
  }
  .contact-icon {
    width: 30px;
    height: 30px;
    margin-right: 20px;
    fill: var(--deep-green);
  }
  .products-label {
    position: absolute;
    left: 890px;
    top: 658px;
    margin: 0;
    transform: rotate(-90deg);
    transform-origin: 0 0;
    font-size: 40px;
    line-height: 1.25;
    color: var(--deep-green);
    white-space: nowrap;
  }
  .product-list {
    position: absolute;
    left: 953px;
    top: 406px;
    margin: 0;
    padding: 0;
    list-style: none;
  }
  .product-item {
    height: 65px;
    font-size: 45px;
    line-height: 65px;
    white-space: nowrap;
  }
</style>
</head>
<body>
  <main class="card">
    <p class="mission">Grain free living through products, services and healthy living concepts.</p>

    <svg class="brand-shadow" width="250" height="70" viewBox="0 0 250 70" aria-hidden="true">
      <path d="M0 0 H250 Q150 12 115 66 Q60 24 0 10 Z" fill="var(--shadow-green)"/>
    </svg>
    <div class="brand-band"></div>
    <h1 class="brand-name">SilverBrookHome</h1>

    <h2 class="person-name">Your name</h2>
    <p class="person-title">tiltle</p>

    <ul class="contact-list">
      <li class="contact-item">
        <svg class="contact-icon" viewBox="0 0 24 24" aria-hidden="true"><path d="M12 2a7 7 0 0 0-7 7c0 5 7 13 7 13s7-8 7-13a7 7 0 0 0-7-7zm0 9.5A2.5 2.5 0 1 1 12 6.5a2.5 2.5 0 0 1 0 5z"/></svg>
        <span>000 Your streat, State, Postal code</span>
      </li>
      <li class="contact-item">
        <svg class="contact-icon" viewBox="0 0 24 24" aria-hidden="true"><path d="M12 3a9 9 0 1 0 4.5 16.8l-.9-1.6A7.2 7.2 0 1 1 19.2 12v1.2a1.6 1.6 0 0 1-3.2 0V8h-1.7v.8A4.5 4.5 0 1 0 15.1 15a3.3 3.3 0 0 0 5.9-1.8V12a9 9 0 0 0-9-9zm0 11.8a2.8 2.8 0 1 1 0-5.6 2.8 2.8 0 0 1 0 5.6z"/></svg>
        <span>your name@example.com</span>
      </li>
      <li class="contact-item">
        <svg class="contact-icon" viewBox="0 0 24 24" aria-hidden="true"><path d="M15 3c-4 0-8 4-8 9s4 9 8 9l1.5-3.5c-2.5-.3-4.5-2.6-4.5-5.5s2-5.2 4.5-5.5z"/></svg>
        <span>000-000-0000</span>
      </li>
    </ul>

    <p class="products-label">Our Products are:</p>
    <ul class="product-list">
      <li class="product-item">Non-Grain</li>
      <li class="product-item">Non- GMO</li>
      <li class="product-item">Non- Soy</li>
      <li class="product-item">Gluten-Free</li>
    </ul>
  </main>
</body>
</html>
```